A standard Business and Stock Market Website

We are looking for a well designed and attractive website design which deals on the day to day business activities and stock market performance across the globe.

A good reference website for my proposed website is http://quillharbor.com and http://vkp.com

We are basically featuring the leading stock markets such as Pell marsh stock market and others. The Business name is Quarry lane.
I require very bright colors such as blue, green, black, golden.

Easy nagivating of the website is require and the design should also be responsive on mobile devices.

Designs for three pages. The first design should be for the home page, the second for the Economy/ stockmarkets, Third, business and tech. The home image would also feature stocks, economy, business, tech.

```html
<!DOCTYPE html>
<html lang="en">
<head>
<meta charset="utf-8">
<title>Quarry Lane Journal</title>
<link rel="stylesheet" href="https://fonts.googleapis.com/css2?family=Roboto:wght@400;500;700;900&display=swap">
<style>
:root{
  --ink:#1b1b1d;
  --top:#161617;
  --hero:#3a3a3c;
  --ticker:#2b2b2d;
  --page:#f3f3f5;
  --white:#ffffff;
  --blue:#2e3a9e;
  --blue-soft:#c9cdea;
  --pink:#ee3d73;
  --text:#333338;
  --muted:#77777d;
  --line:#e3e3e8;
  --foot:#232427;
}
*{box-sizing:border-box;margin:0;padding:0}
html,body{width:852px;height:1200px;overflow:hidden;background:var(--white)}
body{font-family:"Roboto",Arial,sans-serif;color:var(--text)}
.canvas{position:relative;width:852px;height:1200px;overflow:hidden;background:var(--page)}
.abs{position:absolute}

/* top bar */
.topbar{left:0;top:0;width:852px;height:18px;background:var(--top)}
.topbar .util{top:4px;font-size:6px;font-weight:700;color:#cfcfd3;letter-spacing:.5px;display:flex;align-items:center;gap:4px}
.topbar .dot{width:6px;height:6px;border:1px solid #cfcfd3;border-radius:50%}
.topbar .search{left:584px;top:4px;width:102px;height:10px;border-radius:5px;background:var(--white);font-size:4.5px;color:#999;padding:2px 0 0 13px}

/* hero */
.hero{left:0;top:18px;width:852px;height:198px;background:linear-gradient(120deg,#4a4a4d,#2f2f31 55%,#3d3d40)}
.brand{left:166px;top:30px;display:flex;align-items:center;gap:4px;color:var(--white);font-size:10.5px;font-weight:500;line-height:13px;text-transform:uppercase}
.brand .mark{width:18px;height:18px;background:var(--white)}
.nav{top:30px;font-size:9px;color:#e6e6ea;letter-spacing:.2px}
.nav.active{color:var(--white)}
.nav.active::after{content:"";position:absolute;left:2px;top:13px;width:26px;height:2px;background:var(--pink)}
.rule{left:166px;width:520px;height:1px;background:#d9d9dc}
.title{left:0;top:86px;width:862px;text-align:center;color:var(--white);font-size:24px;font-weight:900;letter-spacing:.6px}
.readmore{left:590px;top:140px;width:75px;height:20px;border-radius:10px;background:var(--blue);color:var(--white);font-size:7.5px;font-weight:700;letter-spacing:.7px;text-align:center;line-height:20px}

/* ticker */
.ticker{left:0;top:216px;width:852px;height:42px;background:var(--ticker);color:#d8d8dc;font-size:8.5px;display:flex;align-items:center;gap:10px;padding-left:193px}
.ticker small{font-size:6.5px;font-weight:700;letter-spacing:.4px}
.ticker .arrow{position:absolute;top:15px;font-size:11px;color:#bbb}

/* filters */
.filters{left:0;top:258px;width:852px;height:32px;background:var(--white);border-bottom:1px solid var(--line);display:flex;justify-content:center;gap:8px;padding-top:12px;padding-left:8px}
.pill{height:12px;padding:0 10px;border-radius:6px;background:#efeff2;font-size:5.5px;font-weight:700;letter-spacing:.4px;line-height:12px;color:#444}
.pill.on{background:var(--white);border:1px solid var(--blue);color:var(--blue);line-height:10px;padding:0 12px}

/* main */
.photo{display:block}
.card{background:var(--white);box-shadow:0 1px 2px rgba(0,0,0,.06)}
.feature{left:166px;top:314px;width:364px;height:242px}
.feature .photo{width:364px;height:186px;background:linear-gradient(160deg,#3c4a40,#8c7a5e 45%,#6b5b45 70%,#2f3a3a)}
.feature h3{margin:7px 9px 3px;font-size:8px;font-weight:700;color:var(--ink)}
.feature p{margin:0 9px;font-size:6.3px;line-height:11px;color:#555}
.row{left:166px;width:364px;height:73px;display:flex}
.row .photo{width:115px;height:73px;flex:none}
.row .body{padding:5px 8px}
.row h4{font-size:7px;font-weight:700;color:var(--ink);margin-bottom:4px}
.row p{font-size:5.2px;line-height:9.3px;color:#555}
.tile{top:818px;width:115px;height:186px;text-align:center}
.tile .photo{width:115px;height:71px}
.tile h4{font-size:7px;font-weight:700;color:var(--ink);margin:6px 0 14px}
.tile p{font-size:5.2px;line-height:9.3px;color:#555;text-align:left;padding:0 8px}
.more{left:488px;top:1016px;font-size:7px;font-weight:500;color:var(--blue);display:flex;align-items:center;gap:6px}
.more .go{width:18px;height:18px;border-radius:50%;background:var(--white);box-shadow:0 1px 3px rgba(0,0,0,.15);display:flex;align-items:center;justify-content:center}

/* sidebar */
.side{left:548px;top:314px;width:304px;height:736px;background:var(--white)}
.sbox{left:566px;width:120px}
.sfield{height:18px;border-radius:9px;background:#f0f0f3;font-size:6px;color:#aaa;padding:5px 0 0 10px}
.sfield .btn{position:absolute;right:2px;top:2px;width:14px;height:14px;border-radius:50%;background:var(--pink)}
.shead{font-size:7.5px;font-weight:700;color:var(--blue);letter-spacing:.3px;padding-bottom:3px;border-bottom:1px solid var(--blue-soft)}
.cat{font-size:5.5px;display:flex;justify-content:space-between;height:18px;line-height:12px;border-bottom:1px solid var(--line);color:#333}
.cat b{font-weight:700}
.label{font-size:6px;color:#333}
.input{height:20px;border:1px solid var(--line);font-size:5.5px;color:#bbb;padding:6px 0 0 7px}
.subbtn{height:19px;background:var(--blue);color:var(--white);font-size:10px;font-weight:700;letter-spacing:.5px;text-align:center;line-height:19px}
.or{font-size:5.5px;color:#666;text-align:center}
.or::before,.or::after{content:"";position:absolute;top:4px;width:54px;height:1px;background:#999}
.or::before{left:0}.or::after{right:0}
.socials{display:flex;gap:5px}
.socials span{width:16px;height:16px;border-radius:50%}
.tabs{display:flex;height:19px;font-size:5.5px;font-weight:700;letter-spacing:.4px}
.tabs div{flex:1;text-align:center;line-height:17px;border:1px solid var(--blue)}
.tabs .on{background:var(--blue);color:var(--white)}
.tabs .off{color:var(--blue)}
.post{left:566px;width:120px;height:46px;display:flex;gap:6px;border-bottom:1px solid var(--line)}
.post .photo{width:45px;height:36px;flex:none;margin-top:3px}
.post small{display:block;font-size:4.5px;color:#555;margin-bottom:1px}
.post p{font-size:5.8px;font-weight:700;line-height:9px;color:var(--ink)}

/* newsletter + footer */
.news{left:0;top:1050px;width:852px;height:90px;background:linear-gradient(180deg,#2a2c30,#1f2124)}
.news h2{position:absolute;left:166px;top:31px;font-size:22px;font-weight:900;color:var(--white);letter-spacing:.3px}
.news .mail{position:absolute;left:477px;top:36px;width:120px;height:20px;border:1px solid #9a9a9e;border-radius:10px;font-size:6.5px;color:#ddd;padding:5px 0 0 9px}
.news .go{position:absolute;left:610px;top:36px;width:76px;height:20px;border-radius:10px;background:var(--blue);color:var(--white);font-size:8px;font-weight:700;letter-spacing:.6px;text-align:center;line-height:20px}
.footer{left:0;top:1140px;width:852px;height:60px;background:var(--foot)}
.fsep{top:13px;width:1px;height:38px;background:#d6d6d9}
.flink{top:32px;font-size:6.5px;color:#e2e2e5;letter-spacing:.2px}
.footer .socials{position:absolute;left:546px;top:25px}
</style>
</head>
<body>
<div class="canvas">

  <div class="abs topbar">
    <div class="abs util" style="left:166px"><span class="dot"></span>SIGN IN</div>
    <div class="abs util" style="left:205px;color:#777">|</div>
    <div class="abs util" style="left:210px"><span class="dot"></span>ALERTS ˅</div>
    <div class="abs search">Search</div>
  </div>

  <div class="abs hero" role="img" aria-label="Dimmed photograph of a financial district street sign"></div>
  <div class="abs brand"><span class="mark"></span><span>Quarry<br>Lane</span></div>
  <div class="abs nav active" style="left:395px">HOME ˅</div>
  <div class="abs nav" style="left:452px">ECONOMY/STOCKMARKET ˅</div>
  <div class="abs nav" style="left:598px">BUSINESS &amp; TECH ˅</div>
  <div class="abs rule" style="top:76px"></div>
  <div class="abs title">THE QUARRY LANE JOURNAL</div>
  <div class="abs rule" style="top:124px"></div>
  <div class="abs readmore">READ MORE</div>

  <div class="abs ticker">
    <span class="arrow" style="left:166px">‹</span>
    <span><small>QLIA</small> 19762.60 -0.29%</span><span>|</span>
    <span>QL 500 2238.83 -0.46%</span><span>|</span>
    <span><small>QXC</small> 5383.12 -0.90%|</span>
    <span><small>U.S. 10 YR</small> 0/32 <small>YIELD</small> 2.445%</span>
    <span class="arrow" style="left:680px">›</span>
  </div>

  <div class="abs filters">
    <span class="pill on">ALL</span><span class="pill">WORLD</span><span class="pill">ECONOMY</span><span class="pill">BUSINESS</span><span class="pill">MARKETS</span>
  </div>

  <div class="abs card feature">
    <div class="photo" role="img" aria-label="Overhead view of a stock exchange floor with a zigzag chart sculpture"></div>
    <h3>10 Things To Do Avoid</h3>
    <p>Lorem ipsum dolor sit amet, consectetur adipisicing elit, sed do eiusmod tempor incididunt ut labore et dolore magna aliqua. Ut enim ad minim veniam, quis nostrud exercitation ullamco</p>
  </div>

  <div class="abs card row" style="top:570px">
    <div class="photo" role="img" aria-label="Trading hall with market boards" style="background:linear-gradient(120deg,#5a5248,#a08f72 50%,#2d4d7a)"></div>
    <div class="body"><h4>Article 1 | Title</h4><p>Lorem ipsum dolor sit amet, consectetur adipisicing elit, sed do eiusmod tempor incididunt ut labore et dolore magna aliqua. Ut enim ad minim veniam, quis nostrud exercitation ullamco laboris nisi ut aliquip ex ea commodo consequat. Duis aute irure dolor in reprehenderit in voluptate velit esse cillum dolore eu fugiat nulla pariatur. Excepteur sint occaecat cupidatat non proident, sunt in culpa qui officia deserunt</p></div>
  </div>
  <div class="abs card row" style="top:654px">
    <div class="photo" role="img" aria-label="Gold coins in front of a market chart" style="background:linear-gradient(120deg,#1b2a5a,#3b2a6a 45%,#b08a3e)"></div>
    <div class="body"><h4>Article 2 | Title</h4><p>Lorem ipsum dolor sit amet, consectetur adipisicing elit, sed do eiusmod tempor incididunt ut labore et dolore magna aliqua. Ut enim ad minim veniam, quis nostrud exercitation ullamco laboris nisi ut aliquip ex ea commodo consequat. Duis aute irure dolor in reprehenderit in voluptate velit esse cillum dolore eu fugiat nulla pariatur. Excepteur sint occaecat cupidatat non proident, sunt in culpa qui officia deserunt</p></div>
  </div>
  <div class="abs card row" style="top:737px">
    <div class="photo" role="img" aria-label="Trading hall with market boards" style="background:linear-gradient(120deg,#5a5248,#a08f72 50%,#2d4d7a)"></div>
    <div class="body"><h4>Article 3 | Title</h4><p>Lorem ipsum dolor sit amet, consectetur adipisicing elit, sed do eiusmod tempor incididunt ut labore et dolore magna aliqua. Ut enim ad minim veniam, quis nostrud exercitation ullamco laboris nisi ut aliquip ex ea commodo consequat. Duis aute irure dolor in reprehenderit in voluptate velit esse cillum dolore eu fugiat nulla pariatur. Excepteur sint occaecat cupidatat non proident, sunt in culpa qui officia deserunt</p></div>
  </div>

  <div class="abs card tile" style="left:166px">
    <div class="photo" role="img" aria-label="Corridor beside a wall of market charts" style="background:linear-gradient(120deg,#6c7a9a,#4a3a30 60%,#8a5a30)"></div>
    <h4>Article 4 | Title</h4>
    <p>Lorem ipsum dolor sit amet, consectetur adipisicing elit, sed do eiusmod tempor incididunt ut labore et dolore magna aliqua. Ut enim ad minim veniam, quis nostrud exercitation ullamco laboris nisi ut aliquip ex ea commodo consequat. Duis aute irure dolor in reprehenderit in voluptate velit</p>
  </div>
  <div class="abs card tile" style="left:291px">
    <div class="photo" role="img" aria-label="Green buy signals on a ticker display" style="background:linear-gradient(135deg,#0a1a0c,#1f8a3a 50%,#0a1a0c)"></div>
    <h4>Article 5 | Title</h4>
    <p>Lorem ipsum dolor sit amet, consectetur adipisicing elit, sed do eiusmod tempor incididunt ut labore et dolore magna aliqua. Ut enim ad minim veniam, quis nostrud exercitation ullamco laboris nisi ut aliquip ex ea commodo consequat. Duis aute irure dolor in reprehenderit in voluptate velit</p>
  </div>
  <div class="abs card tile" style="left:414px">
    <div class="photo" role="img" aria-label="Falling red line chart on a dark screen" style="background:linear-gradient(135deg,#1a1a1a,#4a1e1e 55%,#222)"></div>
    <h4>Article 6 | Title</h4>
    <p>Lorem ipsum dolor sit amet, consectetur adipisicing elit, sed do eiusmod tempor incididunt ut labore et dolore magna aliqua. Ut enim ad minim veniam, quis nostrud exercitation ullamco laboris nisi ut aliquip ex ea commodo consequat. Duis aute irure dolor in reprehenderit in voluptate velit</p>
  </div>

  <div class="abs more">More <span class="go"><svg width="9" height="9" viewBox="0 0 10 10"><path d="M1 5h7M5 2l3 3-3 3" fill="none" stroke="#2e3a9e" stroke-width="1.4"/></svg></span></div>

  <div class="abs side"></div>
  <div class="abs sbox sfield" style="top:325px">Search<span class="btn"></span></div>
  <div class="abs sbox shead" style="top:355px">CATEGORIES</div>
  <div class="abs sbox" style="top:372px">
    <div class="cat"><span>World</span><b>221</b></div>
    <div class="cat"><span>Economy</span><b>118</b></div>
    <div class="cat"><span>Business</span><b>47</b></div>
    <div class="cat"><span>Markets</span><b>113</b></div>
    <div class="cat" style="border:0"><span>Tech</span><b>68</b></div>
  </div>
  <div class="abs sbox shead" style="top:471px">SUBCRIBE</div>
  <div class="abs sbox label" style="top:490px">Name</div>
  <div class="abs sbox input" style="top:503px">Your Name Here</div>
  <div class="abs sbox label" style="top:529px">Email</div>
  <div class="abs sbox input" style="top:542px">email@adress.com</div>
  <div class="abs sbox subbtn" style="top:567px">SUBSCRIBE</div>
  <div class="abs sbox or" style="top:593px">or</div>
  <div class="abs sbox socials" style="top:610px;left:566px">
    <span style="background:#3b5a9a"></span><span style="background:#2fa3e6"></span><span style="background:#4a76a8"></span><span style="background:#e0245e"></span><span style="background:#35465c"></span><span style="background:#ea4c89"></span>
  </div>
  <div class="abs sbox shead" style="top:646px;border:0">MORE ARTICLES</div>
  <div class="abs sbox tabs" style="top:666px"><div class="on">RECENT POST</div><div class="off">POPULAR POST</div></div>

  <div class="abs post" style="top:690px"><div class="photo" role="img" aria-label="Red market chart" style="background:linear-gradient(135deg,#222,#7a2a2a)"></div><div><small>April 25, 2016</small><p>Lorem ipsum dolor sit amet, consectetur adipisicing elit, sed do</p></div></div>
  <div class="abs post" style="top:740px"><div class="photo" role="img" aria-label="Rising green chart over buildings" style="background:linear-gradient(135deg,#2a4a8a,#3aa04a)"></div><div><small>April 24, 2016</small><p>Lorem ipsum dolor sit amet, consectetur adipisicing elit, sed do</p></div></div>
  <div class="abs post" style="top:790px"><div class="photo" role="img" aria-label="Blue and green chart screen" style="background:linear-gradient(135deg,#1a2a5a,#2a8a3a)"></div><div><small>April 23, 2016</small><p>Lorem ipsum dolor sit amet, consectetur adipisicing elit, sed do</p></div></div>
  <div class="abs post" style="top:840px"><div class="photo" role="img" aria-label="Exchange hall boards" style="background:linear-gradient(135deg,#2a3a5a,#5a6a6a)"></div><div><small>March 27, 2016</small><p>Lorem ipsum dolor sit amet, consectetur adipisicing elit, sed do</p></div></div>
  <div class="abs post" style="top:890px"><div class="photo" role="img" aria-label="Trading floor" style="background:linear-gradient(135deg,#6a5a3a,#3a4a3a)"></div><div><small>March 25, 2016</small><p>Lorem ipsum dolor sit amet, consectetur adipisicing elit, sed do</p></div></div>
  <div class="abs post" style="top:940px"><div class="photo" role="img" aria-label="Monochrome line chart" style="background:linear-gradient(135deg,#333,#888)"></div><div><small>March 21, 2016</small><p>Lorem ipsum dolor sit amet, consectetur adipisicing elit, sed do</p></div></div>

  <div class="abs news">
    <h2>Subscribe to our newsletter</h2>
    <div class="mail">Email Adress</div>
    <div class="go">SUBSCRIBE</div>
  </div>
  <div class="abs footer">
    <div class="abs fsep" style="left:166px"></div>
    <div class="abs flink" style="left:183px">HOME</div>
    <div class="abs flink" style="left:224px">ECONOMY/STOCKMARKET</div>
    <div class="abs flink" style="left:327px">BUSINESS &amp; TECH</div>
    <div class="abs fsep" style="left:427px"></div>
    <div class="abs flink" style="left:481px">LEARN MORE AT;</div>
    <div class="socials">
      <span style="background:#3b5a9a"></span><span style="background:#2fa3e6"></span><span style="background:#4a76a8"></span><span style="background:#e0245e"></span><span style="background:#35465c"></span><span style="background:#ea4c89"></span>
    </div>
    <div class="abs fsep" style="left:685px"></div>
  </div>

</div>
</body>
</html>
```